Simple Banners for several sites

I'm looking for banners in the following formats for the sites listed bellow:

* Leaderboard
* Wide Skyscraper
* Skyscaper
* Square Button
* Micro bar
* Full banner
* Half Banner
* Medium Rectangle

The websites:
* http://notavault.crenmop.com/
* http://quolet.com/
* http://dravimunto.com/

I would like to get 1 sets of banners for each website, and I'ld like you to submit each set/site independently.

```html
<!DOCTYPE html>
<html lang="en">
<head>
<meta charset="utf-8">
<title>QUOLET banner set</title>
<link rel="stylesheet" href="https://fonts.googleapis.com/css2?family=Lato:wght@400&family=Roboto+Condensed:wght@300;400;700&display=swap">
<style>
:root{
  --stage:#1c1c1c;
  --stage-edge:#141414;
  --white:#ffffff;
  --logo:#3d3a36;
  --url:#8a8378;
  --panel-light:#5a554d;
  --panel-dark:#2f2c28;
  --headline:#e4e0d2;
  --digital-top:#f1eedd;
  --digital-bottom:#bdb69a;
  --body:#ffffff;
  --btn-top:#ffa43a;
  --btn-bottom:#e26a06;
  --btn-text:#ffffff;
  --device-frame:#1e1e1e;
  --device-screen:#e6e5e0;
  --device-accent:#b8302a;
}
*{margin:0;padding:0;box-sizing:border-box}
html,body{width:1200px;height:829px;overflow:hidden;background:radial-gradient(ellipse at 50% 40%,var(--stage),var(--stage-edge))}
.stage{position:absolute;left:0;top:0;width:1118px;height:772px;transform:scale(1.0733);transform-origin:0 0}
.banner{position:absolute;overflow:hidden;box-shadow:0 2px 8px rgba(0,0,0,.6)}
.panel{position:absolute;background:radial-gradient(ellipse at 50% 45%,var(--panel-light),var(--panel-dark))}
.logo-box{position:absolute;background:var(--white);display:flex;align-items:center}
.logo{font-family:"Lato",sans-serif;font-weight:400;color:var(--logo);letter-spacing:1px;white-space:nowrap}
.url{font-family:"Lato",sans-serif;color:var(--url);font-size:14px;white-space:nowrap}
.headline{position:absolute;font-family:"Roboto Condensed",sans-serif;font-weight:300;color:var(--headline);line-height:1.1;text-transform:uppercase;white-space:nowrap;text-align:center}
.headline .digital{display:block;font-weight:700;background:linear-gradient(var(--digital-top),var(--digital-bottom));-webkit-background-clip:text;background-clip:text;color:transparent;line-height:1}
.body-copy{position:absolute;font-family:"Roboto Condensed",sans-serif;color:var(--body);text-align:center;line-height:1.25;white-space:nowrap}
.cta{position:absolute;display:flex;align-items:center;justify-content:center;gap:3px;border-radius:5px;background:linear-gradient(var(--btn-top),var(--btn-bottom));font-family:"Roboto Condensed",sans-serif;font-weight:400;color:var(--btn-text);font-size:21px;white-space:nowrap;box-shadow:0 2px 3px rgba(0,0,0,.5)}
.cta svg{flex:none}
.devices{position:absolute;border-radius:4px;background:
  linear-gradient(var(--device-accent),var(--device-accent)) 30% 35%/40% 22% no-repeat,
  linear-gradient(var(--device-screen),var(--device-screen)) 50% 45%/88% 80% no-repeat,
  var(--device-frame)}
</style>
</head>
<body>
<main class="stage">

  <section class="banner skyscraper" style="left:101px;top:84px;width:160px;height:600px">
    <div class="logo-box" style="left:0;top:0;width:160px;height:70px;justify-content:center">
      <span class="logo" style="font-size:34px">QUOLET</span>
    </div>
    <div class="panel" style="left:0;top:70px;width:160px;height:530px"></div>
    <h2 class="headline" style="left:0;top:102px;width:160px;font-size:22px">Your magazine<br>on everything<span class="digital" style="font-size:44px">Digital</span></h2>
    <div class="devices" role="img" aria-label="Tablet and desktop screen showing the magazine website" style="left:0;top:224px;width:160px;height:176px"></div>
    <p class="body-copy" style="left:0;top:426px;width:160px;font-size:16px">Computers,<br>smartphones and<br>online world at<br>hand's reach QUOLET</p>
    <a class="cta" style="left:11px;top:530px;width:137px;height:38px">LEARN MORE
      <svg width="17" height="17" viewBox="0 0 18 18" aria-hidden="true"><circle cx="9" cy="9" r="8" fill="#fff"/><path d="M5 9h6M8.5 5.5 12 9l-3.5 3.5" stroke="#e26a06" stroke-width="2.2" fill="none"/></svg></a>
    <p class="url" style="position:absolute;left:0;top:574px;width:160px;text-align:center">www.quolet.com</p>
  </section>

  <section class="banner rectangle" style="left:302px;top:243px;width:340px;height:283px">
    <div class="logo-box" style="left:0;top:0;width:340px;height:66px">
      <span class="logo" style="font-size:37px;margin-left:16px">QUOLET</span>
      <span style="width:1px;height:40px;background:var(--logo);margin-left:18px"></span>
      <span class="url" style="margin-left:13px;color:#5e5950">www.quolet.com</span>
    </div>
    <div class="panel" style="left:0;top:66px;width:340px;height:217px"></div>
    <h2 class="headline" style="left:4px;top:74px;width:162px;font-size:22px">Your magazine<br>on everything<span class="digital" style="font-size:42px">Digital</span></h2>
    <p class="body-copy" style="left:4px;top:174px;width:162px;font-size:14px">Computers, smartphones<br>and online world at<br>hand's reach QUOLET</p>
    <a class="cta" style="left:14px;top:233px;width:137px;height:37px">LEARN MORE
      <svg width="17" height="17" viewBox="0 0 18 18" aria-hidden="true"><circle cx="9" cy="9" r="8" fill="#fff"/><path d="M5 9h6M8.5 5.5 12 9l-3.5 3.5" stroke="#e26a06" stroke-width="2.2" fill="none"/></svg></a>
    <div class="devices" role="img" aria-label="Tablet and desktop screen showing the magazine website" style="left:160px;top:86px;width:180px;height:176px"></div>
  </section>

  <section class="banner leaderboard" style="left:302px;top:594px;width:728px;height:90px">
    <div class="logo-box" style="left:0;top:0;width:155px;height:90px;justify-content:center">
      <span class="logo" style="font-size:33px">QUOLET</span>
    </div>
    <div class="panel" style="left:155px;top:0;width:573px;height:90px"></div>
    <h2 class="headline" style="left:163px;top:5px;width:156px;font-size:20px">Your magazine<br>on everything<span class="digital" style="font-size:38px">Digital</span></h2>
    <div class="devices" role="img" aria-label="Tablet and desktop screen showing the magazine website" style="left:326px;top:2px;width:126px;height:84px"></div>
    <p class="body-copy" style="left:452px;top:11px;width:148px;font-size:14px">Computers,<br>smartphones and<br>online world at<br>hand's reach QUOLET</p>
    <a class="cta" style="left:596px;top:21px;width:120px;height:36px">LEARN MORE</a>
    <p class="url" style="position:absolute;left:586px;top:61px;width:140px;text-align:center">www.quolet.com</p>
  </section>

</main>
</body>
</html>
```